Website for Larkwood Fresh Foods

Slogan to be used is Fresh is Best !
I would like the website to be like my other business @ www.tuberhaven.com.au. It is the same business

Industry/Entity Type

Vegetable Processing

Coding

Coded - Design and coding required

Number of Pages Required

1 page

```html
<!DOCTYPE html>
<html lang="en">
<head>
<meta charset="utf-8">
<title>Larkwood Fresh Foods</title>
<link href="https://fonts.googleapis.com/css2?family=League+Gothic&family=Montserrat:wght@400;500;600&display=swap" rel="stylesheet">
<style>
:root{
  --brown:#6a3e1c;
  --orange:#f15a22;
  --page:#f6f6f6;
  --white:#ffffff;
  --ink:#1f1f1f;
  --muted:#444;
  --rule:#dcdcdc;
  --green-1:#dbe9b4;
  --green-2:#c5dc93;
}
*{margin:0;padding:0;box-sizing:border-box}
html,body{width:737px;height:1200px;overflow:hidden}
body{position:relative;background:var(--page);font-family:"Montserrat",sans-serif;color:var(--ink)}
.abs{position:absolute}
.display{font-family:"League Gothic",sans-serif;font-weight:400}

/* header */
.site-header{left:0;top:0;width:737px;height:64px;background:var(--white);z-index:3}
.header-notch{left:331px;top:52px;width:74px;height:30px;background:var(--white);border-radius:50%;z-index:2}
.brand{left:74px;top:14px;display:flex;align-items:center;gap:5px}
.brand-dot{width:14px;height:14px;border-radius:50%;background:var(--orange)}
.brand-name{font-size:9px;font-weight:600;color:var(--orange);line-height:1.15;letter-spacing:.3px}
.nav{left:390px;top:13px;display:flex;align-items:center;font-size:10px;color:#333}
.nav a{text-decoration:none;color:inherit}
.nav .nav-home{width:40px;height:40px;border-radius:50%;background:#f0f6e6;color:var(--orange);display:flex;align-items:center;justify-content:center;margin-right:30px}
.nav .gap{margin-right:33px}

/* hero */
.hero{left:34px;top:64px;width:668px;height:340px;border-radius:0 0 14px 14px;background:linear-gradient(135deg,var(--green-1),var(--green-2) 55%,var(--green-1))}
.hero-copy{left:96px;top:136px;width:220px;text-align:center;color:var(--brown)}
.hero-copy .welcome{font-size:23px;line-height:1}
.hero-copy .title{font-size:35px;line-height:1.05;white-space:nowrap;margin-left:-30px;margin-right:-30px}
.hero-copy .tag{font-size:23px;line-height:1.1}
.btn{display:flex;align-items:center;justify-content:center;background:var(--orange);color:var(--white);font-size:11px;width:106px;height:25px;text-decoration:none}
.hero-btn{left:150px;top:237px}
.hero-photo{left:371px;top:123px;width:307px;height:162px;border-radius:10px;background:linear-gradient(90deg,#e8452c 0 16%,#5b9a2e 16% 32%,#8c1f35 32% 46%,#f2c626 46% 60%,#5f9b3c 60% 72%,#c86fb0 72% 86%,#f2823a 86%)}
.deco{border-radius:50%}
.deco-tomato{left:17px;top:267px;width:57px;height:57px;background:radial-gradient(circle,#f47a6a,#d72a20)}
.deco-carrot{left:647px;top:305px;width:52px;height:52px;background:radial-gradient(circle,#fba13c,#f27a12)}

/* product menu */
.product-menu{left:55px;top:304px;width:192px;height:447px;background:var(--white);border-radius:6px;overflow:hidden;list-style:none;z-index:1}
.product-menu li{height:34.4px;display:flex;align-items:center;justify-content:center;position:relative;font-family:"League Gothic",sans-serif;font-size:16px;letter-spacing:.3px}
.product-menu li:nth-child(even){background:var(--page)}
.product-menu li::after{content:"";position:absolute;right:16px;top:50%;width:5px;height:5px;border-top:1px solid #bbb;border-right:1px solid #bbb;transform:translateY(-50%) rotate(45deg)}
.product-menu li.active{color:var(--brown)}
.product-menu li.active::after{border-color:#333;width:6px;height:6px}

/* product panel */
.panel{background:var(--white);border-radius:10px;overflow:hidden;z-index:1}
.product-panel{left:250px;top:333px;width:422px;height:249px}
.panel-head{left:0;top:10px;width:422px;height:31px;background:var(--page);padding-left:28px;display:flex;align-items:center;color:var(--brown);font-size:19px}
.product-text{left:28px;top:52px;width:385px;font-size:9.1px;line-height:15px;color:#333}
.product-photo{left:28px;top:116px;width:116px;height:86px;border-radius:0 0 58px 58px;background:linear-gradient(180deg,#f7a03a 0 50%,#c98a51 50%)}
.product-points{left:158px;top:121px;width:215px;list-style:none;font-size:8.3px;line-height:15px;color:#333}
.product-points li{padding-left:17px;position:relative;margin-bottom:9px}
.product-points li::before{content:"";position:absolute;left:0;top:3px;width:10px;height:7px;border-radius:0 0 6px 6px;background:#f6a43a}
.product-btn{left:158px;top:205px}

/* call panel */
.call-panel{left:252px;top:593px;width:420px;height:158px;text-align:center}
.call-title{left:0;top:19px;width:420px;font-size:17px;font-weight:500;color:#111}
.call-phone{left:0;top:48px;width:420px;display:flex;justify-content:center;align-items:center;gap:7px;font-size:13px;font-weight:500}
.phone-icon{width:22px;height:22px;border-radius:50%;background:var(--brown);display:flex;align-items:center;justify-content:center}
.slogan-band{left:0;top:94px;width:420px;height:46px;background:var(--page);display:flex;align-items:center;justify-content:center;color:var(--brown);font-size:31px}

/* why */
.why-title{left:76px;top:800px;font-size:26px;color:var(--brown)}
.why-text{left:76px;top:847px;width:318px;font-size:9.4px;line-height:16.7px;color:#333}
.why-btn{left:76px;top:927px}
.why-photo{left:406px;top:813px;width:259px;height:129px;border-radius:4px;background:linear-gradient(100deg,#e64530 0 18%,#5e9d35 18% 45%,#f08a4a 45% 62%,#9fcf6a 62% 80%,#7c4d8f 80%)}
.deco-pumpkin{left:626px;top:791px;width:59px;height:48px;border-radius:6px 6px 30px 30px;background:radial-gradient(circle at 50% 30%,#fbb05c,#f08a14)}

/* footer */
.footer-band{left:0;top:997px;width:737px;height:58px;background:var(--white)}
.veg-row{top:16px;display:flex;gap:1px}
.veg-row span{width:27px;height:27px;border-radius:50%}
.veg-left{left:2px}.veg-right{left:511px}
.footer-brand{left:325px;top:17px}
.footer-links{left:0;top:1055px;width:737px;height:105px}
.link-col{top:28px;list-style:none;font-size:10px;line-height:17px;color:#333}
.foot-call{left:542px;top:27px;color:#8d4b1c;font-size:11px;font-weight:500;line-height:17px}
.foot-phone{left:540px;top:69px;display:flex;align-items:center;gap:5px;font-size:11px}
.foot-phone .phone-icon{width:14px;height:14px}
.footer-rule{left:0;top:1160px;width:737px;height:1px;background:var(--rule)}
.copyright{left:0;top:1161px;width:737px;height:39px;background:var(--white);display:flex;align-items:center;justify-content:center;font-size:8.5px;color:#333}
</style>
</head>
<body>

<header class="abs site-header">
  <div class="abs brand"><span class="brand-dot"></span><span class="brand-name">LARKWOOD<br>FRESH FOODS</span></div>
  <nav class="abs nav">
    <a class="nav-home" href="#">Home</a>
    <a class="gap" href="#">About</a>
    <a class="gap" href="#">Our Customers</a>
    <a href="#">Contact</a>
  </nav>
</header>
<div class="abs header-notch"></div>

<section class="abs hero"></section>
<div class="abs hero-copy display">
  <div class="welcome">Welcome To</div>
  <div class="title">Larkwood Fresh Foods</div>
  <div class="tag">"Fresh is Best!"</div>
</div>
<a class="abs btn hero-btn" href="#">Order Now</a>
<div class="abs hero-photo" role="img" aria-label="Rows of diced fresh vegetables: capsicum, broccoli, beetroot, corn, beans, onion and carrot"></div>
<div class="abs deco deco-tomato" role="img" aria-label="Tomato slice"></div>
<div class="abs deco deco-carrot" role="img" aria-label="Carrot slice"></div>

<ul class="abs product-menu">
  <li>POTATOES</li><li class="active">PUMPKIN</li><li>CARROT</li><li>ONION</li><li>CABBAGE</li><li>CELERY</li><li>CAPSICUM</li><li>ZUCCHINI</li><li>MUSHROOM</li><li>SPINACH</li><li>BROCOLLI</li><li>CAULIFLOWER</li><li>MIXES</li>
</ul>

<section class="abs panel product-panel">
  <h2 class="abs panel-head display">PUMPKIN</h2>
  <p class="abs product-text">Lorem ipsum dolor sit amet, consectetur adipiscing elit, sed do eiusmod tempor incididunt ut labore et dolore magna aliqua. Quis ipsum suspendisse ultrices gravida. Risus commodo viverra maecenas accumsan lacus vel facilisis.</p>
  <div class="abs product-photo" role="img" aria-label="Diced pumpkin in a wooden bowl"></div>
  <ul class="abs product-points">
    <li>Lorem ipsum dolor sit amet, sed do ut labore et dolore magna aliqua.</li>
    <li>Lorem ipsum dolor sit amet, sed do ut labore et dolore magna aliqua.</li>
  </ul>
  <a class="abs btn product-btn" href="#">Order Now</a>
</section>

<section class="abs panel call-panel">
  <h3 class="abs call-title">Call Us Now For Order Vegetables</h3>
  <div class="abs call-phone">
    <span class="phone-icon"><svg width="11" height="11" viewBox="0 0 24 24"><path fill="#fff" d="M6.6 10.8a15.1 15.1 0 0 0 6.6 6.6l2.2-2.2a1 1 0 0 1 1-.25 11.4 11.4 0 0 0 3.6.57 1 1 0 0 1 1 1V20a1 1 0 0 1-1 1A17 17 0 0 1 3 4a1 1 0 0 1 1-1h3.5a1 1 0 0 1 1 1c0 1.250.2 2.450.57 3.57a1 1 0 0 1-.25 1z"/></svg></span>
    <span>+(1) 555 014 2378</span>
  </div>
  <div class="abs slogan-band display">Fresh Is Best!</div>
</section>

<h2 class="abs why-title display">Why Choose Us</h2>
<p class="abs why-text">Lorem ipsum dolor sit amet, consectetur adipiscing elit, sed do eiusmod tempor incididunt ut labore et dolore magna aliqua. Quis ipsum suspendisse ultrices gravida. Risus commodo viverra maecenas accumsan lacus vel facilisis.</p>
<a class="abs btn why-btn" href="#">Read More</a>
<div class="abs why-photo" role="img" aria-label="Assorted chopped vegetables: capsicum, broccoli, carrot, beans, zucchini and eggplant"></div>
<div class="abs deco-pumpkin" role="img" aria-label="Pumpkin slice"></div>

<footer>
  <div class="abs footer-band">
    <div class="abs veg-row veg-left" role="img" aria-label="Row of sliced vegetables">
      <span style="background:#a9d88a"></span><span style="background:#f39a2a"></span><span style="background:#f4e27a"></span><span style="background:#e0392e"></span><span style="background:#7fc04a"></span><span style="background:#b8a0c8"></span><span style="background:#e8302a"></span><span style="background:#f5922a"></span>
    </div>
    <div class="abs brand footer-brand"><span class="brand-dot"></span><span class="brand-name">LARKWOOD<br>FRESH FOODS</span></div>
    <div class="abs veg-row veg-right" role="img" aria-label="Row of sliced vegetables">
      <span style="background:#a9d88a"></span><span style="background:#f39a2a"></span><span style="background:#f4e27a"></span><span style="background:#e0392e"></span><span style="background:#7fc04a"></span><span style="background:#b8a0c8"></span><span style="background:#e8302a"></span><span style="background:#f5922a"></span>
    </div>
  </div>
  <div class="abs footer-links">
    <ul class="abs link-col" style="left:75px"><li>About</li><li>Our Customers</li><li>Contact</li><li>Mixes</li></ul>
    <ul class="abs link-col" style="left:209px"><li>potatoes</li><li>pumpkin</li><li>carrot</li><li>onion</li></ul>
    <ul class="abs link-col" style="left:316px"><li>cabbage</li><li>celery</li><li>capsicum</li><li>zucchini</li></ul>
    <ul class="abs link-col" style="left:426px"><li>mushroom</li><li>spinach</li><li>brocolli</li><li>cauliflower</li></ul>
    <div class="abs foot-call">Call Us Now For Order<br>Vegetables</div>
    <div class="abs foot-phone">
      <span class="phone-icon"><svg width="8" height="8" viewBox="0 0 24 24"><path fill="#fff" d="M6.6 10.8a15.1 15.1 0 0 0 6.6 6.6l2.2-2.2a1 1 0 0 1 1-.25 11.4 11.4 0 0 0 3.6.57 1 1 0 0 1 1 1V20a1 1 0 0 1-1 1A17 17 0 0 1 3 4a1 1 0 0 1 1-1h3.5a1 1 0 0 1 1 1c0 1.250.2 2.450.57 3.57a1 1 0 0 1-.25 1z"/></svg></span>
      <span>(1) 555 014 2378</span>
    </div>
  </div>
  <div class="abs footer-rule"></div>
  <div class="abs copyright">© Copyrights 2023 Larkwood Fresh Foods | All Rights Reserved</div>
</footer>

</body>
</html>
```